Belvant Systems Business Card

Utilize the newly designed logo to create a polished, professional 2-sided business card for this IT Services company.

Target Market(s)

IT Professionals many in the telecommunications and medical industries.

Industry/Entity Type

Business

Requirements
Must have
• Use of new logo, identified color palette and font: Albertus MT Std Regular.

```html
<!DOCTYPE html>
<html lang="en">
<head>
<meta charset="utf-8">
<title>Belvant Systems Business Card</title>
<link rel="stylesheet" href="https://fonts.googleapis.com/css2?family=Marcellus&family=Questrial&display=swap">
<style>
  :root {
    --bg: #e9e9ec;
    --paper: #ffffff;
    --navy: #2a3f97;
    --royal: #3a58b0;
    --sky: #7aa3da;
    --cyan: #35b6e8;
    --ink: #24378c;
  }
  * { box-sizing: border-box; margin: 0; padding: 0; }
  html, body {
    width: 1200px; height: 1000px; overflow: hidden;
    background: var(--bg);
  }
  .canvas { position: relative; width: 1200px; height: 1000px; }
  .card {
    position: absolute;
    width: 700px; height: 400px;
    background: var(--paper);
    overflow: hidden;
    box-shadow: 0 6px 18px rgba(0,0,0,0.12);
  }
  .card--front { left: 80px; top: 70px; }
  .card--back { left: 420px; top: 530px; }

  .wordmark { display: flex; align-items: center; gap: 18px; color: var(--ink); }
  .wordmark__dot {
    width: 62px; height: 62px; border-radius: 50%;
    background: var(--royal);
    flex: none;
  }
  .wordmark__text { font-family: "Marcellus", serif; line-height: 1; text-transform: uppercase; }
  .wordmark__name { display: block; font-size: 44px; letter-spacing: 2px; }
  .wordmark__sub { display: block; font-size: 22px; letter-spacing: 3px; margin-top: 6px; padding-left: 8px; }

  .card--front .wordmark { position: absolute; left: 150px; top: 62px; }

  .holder { position: absolute; left: 0; right: 0; top: 200px; text-align: center; color: var(--ink); }
  .holder__name { font-family: "Questrial", sans-serif; font-size: 36px; }
  .holder__role {
    font-family: "Questrial", sans-serif; font-size: 11px;
    letter-spacing: 9px; text-transform: uppercase; margin-top: 2px;
  }
  .contact { margin-top: 18px; font-family: "Questrial", sans-serif; font-size: 14px; line-height: 1.5; }
  .contact__label { color: var(--navy); }

  .corner { position: absolute; }
  .corner--front-right { right: 0; top: 150px; width: 80px; height: 160px; }
  .corner--back-tl { left: 0; top: 0; width: 160px; height: 60px; }
  .corner--back-tr { right: 0; top: 60px; width: 70px; height: 110px; }
  .corner--back-br { right: 0; bottom: 0; width: 200px; height: 110px; }

  .card--back .wordmark {
    position: absolute; left: 0; right: 0; top: 95px;
    flex-direction: column; gap: 22px; text-align: center;
  }
  .card--back .wordmark__dot { width: 110px; height: 110px; }
  .card--back .wordmark__name { font-size: 50px; }
  .card--back .wordmark__sub { font-size: 24px; padding-left: 0; }
</style>
</head>
<body>
<main class="canvas">

  <section class="card card--front" aria-label="Business card, contact side">
    <div class="wordmark">
      <span class="wordmark__dot"></span>
      <span class="wordmark__text">
        <span class="wordmark__name">Belvant</span>
        <span class="wordmark__sub">Systems</span>
      </span>
    </div>

    <div class="holder">
      <p class="holder__name">Dana Whitfield</p>
      <p class="holder__role">Manager</p>
      <div class="contact">
        <p><span class="contact__label">email:</span> contact@belvant.example</p>
        <p><span class="contact__label">phone:</span> 555 014 2290</p>
      </div>
    </div>

    <svg class="corner corner--front-right" viewBox="0 0 80 160" aria-hidden="true">
      <circle cx="100" cy="80" r="80" fill="var(--sky)"/>
    </svg>
  </section>

  <section class="card card--back" aria-label="Business card, brand side">
    <svg class="corner corner--back-tl" viewBox="0 0 160 60" aria-hidden="true">
      <circle cx="80" cy="-40" r="90" fill="var(--cyan)"/>
    </svg>
    <svg class="corner corner--back-tr" viewBox="0 0 70 110" aria-hidden="true">
      <circle cx="110" cy="55" r="100" fill="var(--navy)"/>
    </svg>
    <svg class="corner corner--back-br" viewBox="0 0 200 110" aria-hidden="true">
      <circle cx="160" cy="150" r="130" fill="var(--sky)"/>
    </svg>

    <div class="wordmark">
      <span class="wordmark__dot"></span>
      <span class="wordmark__text">
        <span class="wordmark__name">Belvant</span>
        <span class="wordmark__sub">Systems</span>
      </span>
    </div>
  </section>

</main>
</body>
</html>
```